Flyer for the Harvest of Lanterns Conference

Flyer design for an annual international conference called "MERIVAL 2017". This is a conference for young adults, so we hope to produce a design that is both professional and appealing to young people in general

We'd like the flyer to showcase the conference brand logo, and clearly highlight the key information to people who will read it.

Target Market(s)

Young people, young adults

Industry/Entity Type

Religious

Font styles to use
Sans Serif

Colors

Designer to choose colors to be used in the design.

Requirements
Must have
• - Should be only one page (Vertical or Horizontal).
• - the MERVAL logo and all the information found in the attached text file. This includes: Main topic: Your sons and daughters shall prophesy,
• Dates and time, location, contact information and everything that is in the attached text file.
Nice to have
• It would be nice to see samples where the white logo is used and another where the black one is used.
Should not have
• This is NOT a folded flyer, we will be sticking it on doors and public places. And we will be printing large simple to put on walls. So only one page with few words like an add (the words are in the attached file)

```html
<!DOCTYPE html>
<html lang="en">
<head>
<meta charset="utf-8">
<title>MERIVAL 2017 Flyer</title>
<link href="https://fonts.googleapis.com/css2?family=Cabin:wght@400;600;700&display=swap" rel="stylesheet">
<style>
  :root {
    --orange: #f39325;
    --orange-deep: #e8581f;
    --black: #111111;
    --ink: #2b2b2b;
    --paper: #ffffff;
    --paper-shade: #e9e9e9;
    --wood-dark: #2a1a10;
    --wood-mid: #6b4427;
    --wood-light: #a5764a;
  }
  html, body {
    margin: 0;
    padding: 0;
    width: 800px;
    height: 1200px;
    overflow: hidden;
    background: var(--paper);
  }
  .flyer {
    position: relative;
    width: 800px;
    height: 1200px;
    overflow: hidden;
    font-family: "Cabin", Arial, sans-serif;
    background: linear-gradient(90deg, var(--paper) 0%, var(--paper) 55%, var(--paper-shade) 100%);
    color: var(--ink);
  }
  .hero {
    position: absolute;
    left: 0; top: 0;
    width: 800px; height: 720px;
  }
  .hero-text {
    position: absolute;
    left: 34px;
    color: #fff;
    text-shadow: 0 3px 6px rgba(0,0,0,.55);
    margin: 0;
  }
  .event-name {
    top: 70px;
    font-size: 62px;
    font-weight: 600;
    letter-spacing: 1px;
  }
  .event-subtitle {
    top: 158px;
    font-size: 25px;
    font-weight: 400;
    letter-spacing: 0.5px;
  }
  .theme {
    top: 252px;
    font-size: 68px;
    font-weight: 700;
    line-height: 86px;
  }
  .speakers-title {
    position: absolute;
    left: 50px; top: 682px;
    margin: 0;
    font-size: 32px;
    font-weight: 700;
    color: var(--orange-deep);
  }
  .speakers-rule {
    position: absolute;
    left: 50px; top: 726px;
    width: 250px; height: 2px;
    background: linear-gradient(90deg, var(--ink), rgba(0,0,0,0));
  }
  .speaker-list {
    position: absolute;
    list-style: none;
    margin: 0; padding: 0;
    font-size: 25px;
    font-weight: 600;
    color: var(--ink);
  }
  .speaker-list li {
    display: flex;
    align-items: center;
    height: 50px;
  }
  .speaker-list svg { margin-right: 14px; }
  .speakers-left { left: 50px; top: 735px; }
  .speakers-right { left: 485px; top: 735px; }
  .info-band {
    position: absolute;
    left: 0; top: 910px;
    width: 560px; height: 212px;
    background: var(--orange);
    color: #fff;
  }
  .info-col {
    position: absolute;
    top: 22px;
  }
  .info-col.dates { left: 50px; width: 150px; }
  .info-col.venue { left: 233px; width: 310px; }
  .info-label {
    font-size: 18px;
    font-weight: 400;
    padding-bottom: 3px;
    margin-bottom: 6px;
    border-bottom: 1px solid rgba(255,255,255,.65);
    opacity: .92;
  }
  .info-value {
    font-size: 19px;
    font-weight: 600;
    line-height: 23px;
    margin-bottom: 12px;
  }
  .brand-fold {
    position: absolute;
    left: 505px; top: 853px;
    width: 0; height: 0;
    border-left: 50px solid transparent;
    border-bottom: 57px solid #6d6d6d;
  }
  .brand-box {
    position: absolute;
    left: 555px; top: 853px;
    width: 230px; height: 269px;
    background: var(--black);
    display: flex;
    flex-direction: column;
    align-items: center;
    justify-content: center;
  }
  .brand-mark {
    width: 56px; height: 56px;
    border-radius: 50%;
    background: var(--orange);
    margin-bottom: 18px;
  }
  .brand-name {
    color: #fff;
    font-size: 36px;
    font-weight: 600;
    letter-spacing: 2px;
  }
  .contact-line {
    position: absolute;
    left: 0; top: 1146px;
    width: 800px;
    text-align: center;
    font-size: 18px;
    font-weight: 700;
    color: var(--black);
  }
</style>
</head>
<body>
<main class="flyer">
  <svg class="hero" viewBox="0 0 800 720" width="800" height="720">
    <defs>
      <linearGradient id="woodTone" x1="0" y1="0" x2="0" y2="1">
        <stop offset="0" stop-color="var(--wood-dark)"/>
        <stop offset="0.45" stop-color="var(--wood-mid)"/>
        <stop offset="0.75" stop-color="var(--wood-light)"/>
        <stop offset="1" stop-color="var(--wood-mid)"/>
      </linearGradient>
      <linearGradient id="bookTone" x1="0" y1="0" x2="1" y2="0">
        <stop offset="0" stop-color="#000" stop-opacity="0"/>
        <stop offset="0.55" stop-color="#000" stop-opacity="0"/>
        <stop offset="0.7" stop-color="#8a2a1e" stop-opacity="0.55"/>
        <stop offset="1" stop-color="#d9a55a" stop-opacity="0.6"/>
      </linearGradient>
    </defs>
    <path d="M0 568 Q380 836 800 528" fill="none" stroke="var(--orange)" stroke-width="12"/>
    <g role="img" aria-label="Photo of a stack of old books on a wooden table">
      <path d="M0 0 H800 V520 Q380 828 0 560 Z" fill="url(#woodTone)"/>
      <path d="M0 0 H800 V520 Q380 828 0 560 Z" fill="url(#bookTone)"/>
    </g>
    <path d="M0 560 Q380 828 800 520" fill="none" stroke="var(--black)" stroke-width="5"/>
  </svg>

  <h1 class="hero-text event-name">MERIVAL 2017</h1>
  <p class="hero-text event-subtitle">HARVEST OF LANTERNS CONFERENCE</p>
  <h2 class="hero-text theme">Your Sons and<br>Daughters Shall<br>Prophesy</h2>

  <h3 class="speakers-title">Speakers:</h3>
  <div class="speakers-rule"></div>
  <ul class="speaker-list speakers-left">
    <li><svg width="20" height="20" viewBox="0 0 20 20"><circle cx="9" cy="11" r="7" fill="none" stroke="var(--orange-deep)" stroke-width="1.6"/><path d="M5 10 L9 14 L18 3" fill="none" stroke="var(--orange-deep)" stroke-width="2"/></svg>Prophet Marcel Odunga</li>
    <li><svg width="20" height="20" viewBox="0 0 20 20"><circle cx="9" cy="11" r="7" fill="none" stroke="var(--orange-deep)" stroke-width="1.6"/><path d="M5 10 L9 14 L18 3" fill="none" stroke="var(--orange-deep)" stroke-width="2"/></svg>Prophet Emmanuel Ren Tabala</li>
    <li><svg width="20" height="20" viewBox="0 0 20 20"><circle cx="9" cy="11" r="7" fill="none" stroke="var(--orange-deep)" stroke-width="1.6"/><path d="M5 10 L9 14 L18 3" fill="none" stroke="var(--orange-deep)" stroke-width="2"/></svg>Prophet Joel</li>
  </ul>
  <ul class="speaker-list speakers-right">
    <li><svg width="20" height="20" viewBox="0 0 20 20"><circle cx="9" cy="11" r="7" fill="none" stroke="var(--orange-deep)" stroke-width="1.6"/><path d="M5 10 L9 14 L18 3" fill="none" stroke="var(--orange-deep)" stroke-width="2"/></svg>Bishop Aaron Mulenda</li>
    <li><svg width="20" height="20" viewBox="0 0 20 20"><circle cx="9" cy="11" r="7" fill="none" stroke="var(--orange-deep)" stroke-width="1.6"/><path d="M5 10 L9 14 L18 3" fill="none" stroke="var(--orange-deep)" stroke-width="2"/></svg>Prophet Elie Tavero</li>
  </ul>

  <section class="info-band">
    <div class="info-col dates">
      <div class="info-label">Senga Date:</div>
      <div class="info-value">September 1st,<br>2nd and<br>3rd 2017</div>
      <div class="info-label">Start Time:</div>
      <div class="info-value">6:00PM</div>
    </div>
    <div class="info-col venue">
      <div class="info-label">Location:</div>
      <div class="info-value">Lakeview Harbor Inn<br>410 Elm Street<br>Brookfield, ME 04199 United</div>
      <div class="info-label">States Room:</div>
      <div class="info-value">Cedar Ballroom</div>
    </div>
  </section>

  <div class="brand-fold"></div>
  <div class="brand-box">
    <div class="brand-mark"></div>
    <div class="brand-name">MERVAL</div>
  </div>

  <p class="contact-line">Tel:+1 (555) 014 2290 | Email:contact@lanternhall.org | Website: http://merival.org</p>
</main>
</body>
</html>
```